Awesome aussie startup needs a mobile/tablet web design

An awesome startup needs a mobile friendly web design for a really simple idea.

We are called "Blorvex.com". It stands for "Silly Queries".

What is this project????
This is the web application where friends, co-workers, teenagers etc will go and post a question like:
"Where are we going for lunch tomorrow?", "Who is coming for a movie this Thursday night?"

The creator of the question will create a question with possible answer/opinion that he has and then send the link of this short, stupid, simple BUT Important question to his/her friends. His/her friends will add short answers or vote for existing answers.

At the end of it, the whole friends group will know who is coming or which place most of us want to go and they have a decision!!

What do we need???
1. [Login page design] - A clean & clear login page with some artwork & a place to login/register with only friendloop, searchly or chirpnet logins. No registration forms etc..

2. [Page with question & answers] - A webpage design that suites the mobile/tablet interface where user can see the 'stupid question' and its answers. A plus/add button that allows the user to add answer to the question in max 70 characters. If user wants to like/vote an answer then he/she can click/tap on the existing answer and its voted/liked. Mockup is available here - https://files.boxvaultcdn.example/u/58310947/newMockup.png

Not required (but submit anyway if you have something!! ) -
1. [Logo] - We want a creative logo that captures imagination! The name of the website itself (Blorvex.com) is creative so a logo should be creative too!! The name Blorvex is derived from "Silly queries" where 'd' from 'Stupid' is flipped to create 'q'. Any other fun and creative variation of it for logo is also open for consideration. Show us your inner creative genius!!!
Updates

Hi Everyone,

Thanks heaps for all of you who have started working on it and have submitted as well.
To make the most of the web design skills I'm removing the logo design from the requirement. A login page and question page are the things we are looking for. If you have both of them in your designs you qualify.

Also, I'll be extending the end date for few more days to accomodate the change.
Do not hesitate to contact if you have questions or queries.
cheers,

Reason: The logo design has been removed. We didn't realise that logo and web design in a single project will confuse the crowd & they are two different skills that designers specialise in. We'll be posting a logo only design project separately to achieve it now. I think the reduction in the scope deserves a reasonable time extension so you guys can complete the work nicely.

Target Market(s)

A friend's group, co-workers, college groups, anyone who tries to organise an event or wants opinion from other known friends.

Industry/Entity Type

Movie

Requirements
Must have
• Login & Question page. Both of the above mentioned pages with modern look.
Nice to have
• A design that works for desktop screen size too!

```html
<!DOCTYPE html>
<html lang="en">
<head>
<meta charset="utf-8">
<title>Blorvex – login and question screens</title>
<link href="https://fonts.googleapis.com/css2?family=Lexend:wght@400;600&family=Roboto:wght@300;400&display=swap" rel="stylesheet">
<style>
  :root {
    --page-bg: #ffffff;
    --plum-dark: #14060c;
    --wine: #5a1427;
    --raspberry: #b8283f;
    --magenta: #8c1a5a;
    --violet: #6d1660;
    --ember: #d9643a;
    --ink-white: #ffffff;
    --soft-white: rgba(255,255,255,0.82);
    --deep-wine: #4a0d22;
    --bar-black: #000000;
    --panel-tint: rgba(255,255,255,0.16);
    --row-line: rgba(255,255,255,0.25);
    --highlight: rgba(255,255,255,0.55);
    --photo-tone: #6b4a3c;
  }
  * { box-sizing: border-box; margin: 0; padding: 0; }
  html, body {
    width: 1200px; height: 1075px; overflow: hidden;
    background: var(--page-bg);
    font-family: "Roboto", Arial, sans-serif;
  }
  .canvas { position: relative; width: 1200px; height: 1075px; }
  .screen {
    position: absolute; top: 299px; width: 323px; height: 484px;
    overflow: hidden; color: var(--ink-white);
  }

  /* Login screen */
  .login {
    left: 203px;
    background:
      radial-gradient(ellipse 70% 45% at 50% 62%, rgba(200,45,70,0.95), transparent 70%),
      radial-gradient(ellipse 60% 50% at 100% 100%, var(--violet), transparent 70%),
      radial-gradient(ellipse 50% 40% at 0% 100%, var(--ember), transparent 70%),
      linear-gradient(180deg, var(--plum-dark) 0%, var(--wine) 35%, var(--raspberry) 70%, var(--magenta) 100%);
  }
  .login .brand {
    position: absolute; top: 104px; left: 0; width: 100%;
    text-align: center;
    font-family: "Lexend", Arial, sans-serif; font-weight: 600;
    font-size: 40px; color: var(--ink-white); letter-spacing: 0.5px;
  }
  .login .tagline {
    position: absolute; top: 229px; left: 0; width: 100%;
    text-align: center; font-weight: 300; font-size: 25px; line-height: 32px;
    color: var(--soft-white);
  }
  .login .divider {
    position: absolute; top: 330px; left: 35px; width: 253px; height: 1px;
    background: linear-gradient(90deg, transparent, rgba(255,255,255,0.6), transparent);
  }
  .login .sign-in {
    position: absolute; top: 396px; left: 0; width: 100%;
    display: flex; justify-content: center; gap: 14px;
  }
  .sign-in .provider {
    font-family: "Lexend", Arial, sans-serif; font-weight: 600;
    font-size: 13px; color: var(--ink-white);
    display: flex; align-items: center; gap: 5px;
  }
  .sign-in .provider::before {
    content: ""; width: 9px; height: 9px; background: var(--ink-white);
  }

  /* Question screen */
  .question-page {
    left: 677px;
    background:
      radial-gradient(ellipse 60% 40% at 60% 25%, rgba(170,35,55,0.9), transparent 70%),
      radial-gradient(ellipse 60% 40% at 0% 85%, var(--ember), transparent 70%),
      linear-gradient(180deg, var(--plum-dark) 0%, var(--wine) 25%, var(--raspberry) 60%, var(--magenta) 100%);
  }
  .topbar {
    position: absolute; top: 0; left: 0; width: 100%; height: 42px;
    background: var(--bar-black);
  }
  .topbar .brand-mini {
    position: absolute; left: 16px; top: 13px;
    font-family: "Lexend", Arial, sans-serif; font-weight: 600; font-size: 13px;
    color: var(--ink-white);
  }
  .topbar .settings { position: absolute; right: 16px; top: 8px; width: 26px; height: 26px; }

  .profile { position: absolute; top: 89px; left: 15px; display: flex; align-items: center; }
  .profile .avatar {
    width: 56px; height: 56px; border: 2px solid var(--ink-white);
    background: linear-gradient(160deg, #8a6a58, var(--photo-tone) 60%, #3a2520);
  }
  .profile .who { margin-left: 16px; margin-top: 18px; }
  .profile .name { font-family: "Lexend", Arial, sans-serif; font-size: 18px; line-height: 20px; }
  .profile .place { font-size: 13px; color: var(--soft-white); }

  .qa-panel {
    position: absolute; top: 159px; left: 0; width: 100%; height: 264px;
    background: var(--panel-tint);
  }
  .qa-panel .ask { position: absolute; top: 12px; left: 14px; right: 16px; }
  .ask .bubble { position: absolute; left: 0; top: 0; width: 32px; height: 28px; }
  .ask .text {
    margin-left: 42px; font-family: "Lexend", Arial, sans-serif; font-weight: 600;
    font-size: 19px; line-height: 24px; letter-spacing: 0.4px;
  }
  .ask .author { text-align: right; font-size: 12px; color: #1a0508; margin-top: 5px; }
  .ask .author b { font-family: "Lexend", Arial, sans-serif; font-weight: 600; }

  .answers { position: absolute; top: 90px; left: 0; width: 100%; list-style: none; }
  .answers li {
    position: relative; height: 36px; padding-left: 56px;
    font-size: 19px; line-height: 36px; border-top: 1px solid var(--row-line);
  }
  .answers li.voted {
    background: linear-gradient(90deg, rgba(255,255,255,0.3), var(--highlight) 70%, rgba(255,255,255,0.35));
    color: var(--deep-wine); font-family: "Lexend", Arial, sans-serif;
  }
  .answers li.voted svg { position: absolute; left: 14px; top: 6px; width: 30px; height: 26px; }
  .answers .row-end { height: 1px; background: var(--row-line); margin-top: 1px; }
  .add-answer {
    position: absolute; top: 208px; right: 29px; width: 27px; height: 27px;
    background: var(--ink-white); color: #222; font-size: 22px; line-height: 26px;
    text-align: center; font-weight: 400;
  }

  .share-bar {
    position: absolute; top: 423px; left: 0; width: 100%; height: 61px;
    border-top: 1px solid var(--row-line);
    background: linear-gradient(90deg, var(--ember) 0%, #c0304a 45%, #a0123f 100%);
    padding: 15px 0 0 15px;
  }
  .share-bar .networks { font-family: "Lexend", Arial, sans-serif; font-weight: 600; font-size: 13px; }
  .share-bar .link { font-size: 13px; color: var(--soft-white); }
</style>
</head>
<body>
<main class="canvas">

  <section class="screen login" aria-label="Login screen">
    <div class="brand">blorvex?</div>
    <p class="tagline">There are no<br>silly Queries.</p>
    <div class="divider"></div>
    <nav class="sign-in" aria-label="Sign in with">
      <span class="provider">friendloop</span>
      <span class="provider">searchly</span>
      <span class="provider">chirpnet</span>
    </nav>
  </section>

  <section class="screen question-page" aria-label="Question screen">
    <header class="topbar">
      <span class="brand-mini">blorvex?</span>
      <svg class="settings" viewBox="0 0 26 26" aria-label="Settings">
        <g fill="#ddd">
          <circle cx="13" cy="13" r="8.5"/>
          <g>
            <rect x="11" y="1" width="4" height="5"/><rect x="11" y="20" width="4" height="5"/>
            <rect x="1" y="11" width="5" height="4"/><rect x="20" y="11" width="5" height="4"/>
            <rect x="11" y="1" width="4" height="5" transform="rotate(45 13 13)"/>
            <rect x="11" y="20" width="4" height="5" transform="rotate(45 13 13)"/>
            <rect x="1" y="11" width="5" height="4" transform="rotate(45 13 13)"/>
            <rect x="20" y="11" width="5" height="4" transform="rotate(45 13 13)"/>
          </g>
        </g>
        <circle cx="13" cy="13" r="3.5" fill="#000"/>
      </svg>
    </header>

    <div class="profile">
      <div class="avatar" role="img" aria-label="Profile photo of the question creator"></div>
      <div class="who">
        <div class="name">Lena Marsh</div>
        <div class="place">Toronto, Canada.</div>
      </div>
    </div>

    <div class="qa-panel">
      <div class="ask">
        <svg class="bubble" viewBox="0 0 32 28" aria-hidden="true">
          <path d="M16 2C8 2 2 6.5 2 12s4 8.5 9 9.5L9 27l7-5.5c8 0 14-4.5 14-9.5S24 2 16 2z" fill="#fff"/>
        </svg>
        <p class="text">Where are we going for Lunch today?</p>
        <p class="author"><b>Tom R.</b> Toronto</p>
      </div>
      <ul class="answers">
        <li>Hotel on flinders lane</li>
        <li class="voted">
          <svg viewBox="0 0 30 26" aria-label="Voted">
            <path d="M15 25C6 18 1 13 1 7.5 1 3.5 4 1 7.5 1c3 0 5.5 2 7.5 4.5C17 3 19.5 1 22.5 1 26 1 29 3.5 29 7.5 29 13 24 18 15 25z" fill="#fff"/>
          </svg>
          Indian Palace
        </li>
        <li>Pollo’s on King St.</li>
        <li class="row-end"></li>
      </ul>
      <div class="add-answer" role="button" aria-label="Add answer">+</div>
    </div>

    <footer class="share-bar">
      <p class="networks">Share on friendloop, searchly, chirpnet</p>
      <p class="link">Share via URL http://blorvex.com/aldfjka</p>
    </footer>
  </section>

</main>
</body>
</html>
```